Business Card Design Project

Basic business card with minimal details. I just need company name, email & web address, telephone and my name.
I would like the back of the card to be grey with my logo & company name centred.

Target Market(s)

Architects
Builders
Property Developers

Industry/Entity Type

Business

Font styles to use
Sans Serif

Colors

Designer to choose colors to be used in the design.

Requirements
Must have
• Framewise Build
Marcus Helby - Director
M: 0427 593184
E: marcus@framewisebuild.com.au
W: www.framewisebuild.com.au
Should not have
• No other images or pictures

```html
<!DOCTYPE html>
<html lang="en">
<head>
<meta charset="utf-8">
<title>Framewise Build – Business Card</title>
<link rel="stylesheet" href="https://fonts.googleapis.com/css2?family=PT+Sans:wght@400&family=Tinos:wght@400&display=swap">
<style>
  :root {
    --bg-dark: #26292d;
    --bg-mid: #3a3e43;
    --bg-light: #575b60;
    --frame: #1c1e21;
    --bar-dark: #1f2225;
    --lime: #b5ff00;
    --white: #ffffff;
    --ink: #101010;
    --brand-slate: #34505e;
  }
  html, body {
    margin: 0;
    padding: 0;
    overflow: hidden;
    background: #e9e9e9;
  }
  .card {
    position: relative;
    width: 1200px;
    height: 693px;
    overflow: hidden;
    font-family: "PT Sans", sans-serif;
  }
  .card__backdrop {
    position: absolute;
    inset: 0;
    background:
      linear-gradient(115deg, transparent 38%, rgba(255,255,255,0.10) 48%, transparent 60%),
      linear-gradient(70deg, transparent 55%, rgba(255,255,255,0.08) 68%, transparent 80%),
      radial-gradient(ellipse at 55% 20%, var(--bg-light) 0%, var(--bg-mid) 45%, var(--bg-dark) 100%);
  }
  .holder {
    position: absolute;
    right: 39px;
    top: 96px;
    margin: 0;
    font-weight: 400;
    font-size: 44px;
    letter-spacing: -1.5px;
    color: var(--white);
    text-transform: uppercase;
    line-height: 1;
  }
  .role-bar {
    position: absolute;
    left: 828px;
    top: 162px;
    width: 372px;
    height: 57px;
    background: var(--lime);
    display: flex;
    align-items: center;
    padding-left: 21px;
    box-sizing: border-box;
    font-size: 30px;
    color: var(--ink);
  }
  .brand-frame {
    position: absolute;
    left: 0;
    top: 369px;
    width: 391px;
    height: 278px;
    background: var(--frame);
  }
  .brand-panel {
    position: absolute;
    left: 12px;
    top: 379px;
    width: 371px;
    height: 259px;
    background: var(--white);
    display: flex;
    align-items: center;
    justify-content: center;
    gap: 14px;
  }
  .brand-panel__mark {
    width: 26px;
    height: 26px;
    background: var(--brand-slate);
  }
  .brand-panel__name {
    font-size: 34px;
    color: var(--brand-slate);
    text-transform: uppercase;
    letter-spacing: 1px;
  }
  .company-bar {
    position: absolute;
    left: 404px;
    top: 372px;
    width: 796px;
    height: 81px;
    background: var(--bar-dark);
    display: flex;
    align-items: center;
    padding-left: 30px;
    box-sizing: border-box;
  }
  .company-bar__name {
    margin: 0;
    font-family: "Tinos", serif;
    font-weight: 400;
    font-size: 44px;
    color: var(--white);
    text-transform: uppercase;
    letter-spacing: 0.5px;
    word-spacing: 8px;
  }
  .contact-box {
    position: absolute;
    left: 404px;
    top: 465px;
    width: 796px;
    height: 182px;
    background: var(--lime);
    padding: 18px 0 0 30px;
    box-sizing: border-box;
  }
  .contact-box__list {
    list-style: none;
    margin: 0;
    padding: 0;
    font-size: 25px;
    line-height: 41px;
    color: var(--ink);
  }
</style>
</head>
<body>
  <div class="card">
    <div class="card__backdrop" role="img" aria-label="Dark carbon-weave texture crossed by soft grey light beams"></div>

    <h1 class="holder">Marcus Helby</h1>
    <div class="role-bar">Director</div>

    <div class="brand-frame"></div>
    <div class="brand-panel">
      <span class="brand-panel__mark"></span>
      <span class="brand-panel__name">Framewise Build</span>
    </div>

    <div class="company-bar">
      <h2 class="company-bar__name">Framewise Build</h2>
    </div>

    <div class="contact-box">
      <ul class="contact-box__list">
        <li>Marcus Helby - Director</li>
        <li>Mobiles : 0427 593184</li>
        <li>E-mail : marcus@framewisebuild.com.au</li>
        <li>Web : www.framewisebuild.com.au</li>
      </ul>
    </div>
  </div>
</body>
</html>
```